Verdalo sage- referral cards for new customers

Hey,

I would like 1 set of business cards with the following details:

10% off any sales / coupon code
Our phone number: 5302749186
Menu :Verdalosage.example (for the menu)
A line left blank to hand write an activation code: either on top or just on one side

Include the Verdalo Sage logo ( your choice of black or white logo)
This card is to drive orders for people to order a cannabis order with Verdalo Sage. Please make the logo a large part of the card on both sides.

Target Market(s)

People who consume cannabis 21 and up

Industry/Entity Type

Business

Contact Information for Business Card

This business card will be given to customers so they can then give it to other customers and generate referalls. We need this card to be elegant, impressionable, professional, and something worth keeping and passing to friends.

Font styles to use
Decorative
Script

Colors
33a6d7
85acd3
3176b5
0455a3
0592cd
85cae6
cee9f5
eaf1f7
757575

Requirements
Must have
• Our website
• Phone Number
• The 10% off an order
• Spot for activation code
Nice to have
• Eye catching design
• Look classy
• Textured feel or textured look
Should not have
• Do not look super cannabis heady
• Do not look attractive to children

```html
<!DOCTYPE html>
<html lang="en">
<head>
<meta charset="utf-8">
<title>Verdalo Sage – Referral Cards</title>
<link href="https://fonts.googleapis.com/css2?family=Archivo+Black&family=Federo&family=Roboto+Condensed:wght@700&display=swap" rel="stylesheet">
<style>
  :root {
    --olive: #545410;
    --flame: #ff4019;
    --gold: #ffb400;
    --ink: #111111;
    --paper: #ffffff;
    --slot-line: #c9c9c9;
    --art-a: #8fd9e4;
    --art-b: #4f5a1c;
  }
  html, body {
    margin: 0;
    padding: 0;
    width: 1200px;
    height: 1200px;
    overflow: hidden;
    background: var(--paper);
  }
  .sheet { position: relative; width: 1200px; height: 1200px; }
  .card {
    position: absolute;
    left: 163px;
    width: 840px;
    height: 480px;
    background: var(--paper);
    border: 2px solid var(--ink);
    box-sizing: border-box;
    box-shadow: 6px 10px 14px rgba(0,0,0,0.22);
    overflow: hidden;
  }
  .card--front { top: 83px; }
  .card--back { top: 637px; }
  .card__shapes { position: absolute; inset: 0; width: 100%; height: 100%; }
  .offer { position: absolute; font-family: "Archivo Black", sans-serif; line-height: 1; }
  .offer__pct { position: absolute; font-size: 108px; letter-spacing: -3px; white-space: nowrap; }
  .offer__off { position: absolute; font-size: 74px; letter-spacing: -2px; white-space: nowrap; }
  .offer__small { position: absolute; font-size: 34px; line-height: 0.9; letter-spacing: -1px; }
  .brand-name {
    position: absolute;
    font-family: "Federo", sans-serif;
    font-size: 54px;
    color: var(--ink);
    white-space: nowrap;
    text-align: center;
  }
  .contact {
    position: absolute;
    font-family: "Roboto Condensed", sans-serif;
    font-weight: 700;
    text-align: center;
    line-height: 1;
    white-space: nowrap;
  }
  .contact__web { font-size: 35px; letter-spacing: -0.5px; }
  .contact__phone { font-size: 48px; margin-top: 18px; }
  .emblem { position: absolute; border-radius: 50%; }

  .card--front .offer, .card--front .contact { color: var(--flame); }
  .card--back .offer, .card--back .contact { color: var(--gold); }
</style>
</head>
<body>
<div class="sheet">

  <section class="card card--front">
    <svg class="card__shapes" viewBox="0 0 836 476" aria-hidden="true">
      <path d="M0 0 H485 Q405 70 394 181 L400 327 Q420 420 485 476 H0 Z" fill="var(--olive)"/>
      <rect x="100" y="181" width="300" height="146" fill="var(--paper)"/>
      <rect x="-20" y="42" width="120" height="396" rx="16" fill="var(--paper)"/>
      <rect x="-20" y="52" width="110" height="376" rx="12" fill="none" stroke="var(--slot-line)" stroke-width="2"/>
    </svg>

    <div class="offer">
      <span class="offer__pct" style="left:132px;top:4px;">10%</span>
      <span class="offer__off" style="left:138px;top:94px;">Off</span>
      <span class="offer__small" style="left:266px;top:96px;">any<br>sales</span>
    </div>

    <div class="brand-name" style="left:100px;top:222px;width:318px;">Verdalo Sage</div>

    <div class="contact" style="left:106px;top:364px;width:300px;">
      <div class="contact__web">verdalosage.example</div>
      <div class="contact__phone">5302749186</div>
    </div>

    <div class="emblem" role="img" aria-label="Brand illustration area"
         style="left:420px;top:60px;width:410px;height:370px;background:radial-gradient(circle, var(--art-a) 0%, var(--art-a) 30%, var(--art-b) 75%, rgba(84,84,16,0) 100%);"></div>
  </section>

  <section class="card card--back">
    <svg class="card__shapes" viewBox="0 0 836 476" aria-hidden="true">
      <path d="M353 0 H836 V476 H353 Q425 410 443 325 L443 178 Q420 70 353 0 Z" fill="var(--flame)"/>
      <rect x="443" y="178" width="300" height="147" fill="var(--paper)"/>
      <rect x="736" y="42" width="130" height="396" rx="16" fill="var(--paper)"/>
      <rect x="746" y="52" width="120" height="376" rx="12" fill="none" stroke="var(--slot-line)" stroke-width="2"/>
    </svg>

    <div class="offer">
      <span class="offer__pct" style="left:452px;top:4px;">10%</span>
      <span class="offer__off" style="left:458px;top:94px;">Off</span>
      <span class="offer__small" style="left:586px;top:96px;">any<br>sales</span>
    </div>

    <div class="brand-name" style="left:428px;top:222px;width:318px;">Verdalo Sage</div>

    <div class="contact" style="left:440px;top:364px;width:290px;">
      <div class="contact__web">verdalosage.example</div>
      <div class="contact__phone">5302749186</div>
    </div>

    <div class="emblem" role="img" aria-label="Brand illustration area"
         style="left:8px;top:56px;width:410px;height:370px;background:radial-gradient(circle, var(--art-a) 0%, var(--art-a) 30%, var(--art-b) 75%, rgba(84,84,16,0) 100%);"></div>
  </section>

</div>
</body>
</html>
```